Website Design for new business Junior Stride Athletics

We need a website for our new business Junior Stride Athletics which is about teaching kids from 5 years to 16 years of age how to play either Australian Rules Football or Soccer. Need area for Soccer and Football plus Coaches section, and schedule for each training etc. NEW LOGO ADDED

Target Market(s)

Adults with kids from 5 to 16 looking for specialist coaches to train their kids

Industry/Entity Type

Fitness

Number of Pages Required

5+ page

Colors
3176b5
ffc214

Requirements
Must have
• Logo
• How, Why and What
Nice to have
• I like this website http://www.bramblewickgames.com.au/
• http://www.quillhavenplaydrills.com.au/ is another site that is okay
Should not have
• Our competitor is this website http://www.marrowvaleyouthclinic.com.au/ but I don't like their website style not kid or parent friendly

```html
<!DOCTYPE html>
<html lang="en">
<head>
<meta charset="utf-8">
<title>Junior Stride Athletics – Where Kids are Champions</title>
<link rel="stylesheet" href="https://fonts.googleapis.com/css2?family=Carlito:wght@400;700&family=Exo+2:wght@400;500;600&display=swap">
<style>
:root{
  --navy:#232d6b;
  --navy-deep:#1b2456;
  --gold:#fdb913;
  --orange:#f7941d;
  --green-btn:#12b24b;
  --green-dark:#0b3d1d;
  --grass-a:#3f7d1f;
  --grass-b:#6aa632;
  --field-a:#a9b59c;
  --field-b:#c9cfc0;
  --stadium-a:#1c2c4a;
  --stadium-b:#3c5a7a;
  --light:#f3f3f3;
  --footer:#2b2b2b;
  --white:#ffffff;
}
*{box-sizing:border-box;margin:0;padding:0}
html,body{width:704px;height:1200px;overflow:hidden;background:var(--white)}
body{position:relative;font-family:"Exo 2",sans-serif;color:var(--white)}
.abs{position:absolute}

.site-header{left:0;top:0;width:704px;height:56px;background:var(--navy);border-bottom:2px solid #2e8b3a}
.brand{top:12px;width:70px;text-align:center;font:600 9px/1.2 "Exo 2",sans-serif;color:var(--white)}
.brand-left{left:20px}.brand-right{right:20px}
.tagline{left:0;width:704px;top:14px;text-align:center;font:700 24px/1 "Carlito",sans-serif;color:var(--gold)}

.hero{left:0;top:56px;width:704px;height:314px;background:linear-gradient(180deg,var(--field-b),var(--field-a))}
.hero-title{left:0;width:704px;top:54px;text-align:center;font:700 29px/37px "Carlito",sans-serif;color:var(--navy-deep)}
.hero-question{left:0;width:704px;top:143px;text-align:center;font:700 13px/17px "Carlito",sans-serif;color:var(--navy-deep)}
.hero-question a{color:var(--navy-deep)}
.trial-btn{left:216px;top:209px;width:262px;height:34px;background:var(--green-btn);border-radius:3px;text-align:center;font:700 22px/34px "Carlito",sans-serif;color:var(--green-dark)}

.grass-band{left:0;width:704px;background:linear-gradient(180deg,var(--grass-b),var(--grass-a))}
.values{top:370px;height:183px}
.card{top:28px;width:186px;height:127px;border-radius:4px;padding:12px 6px 0;text-align:center}
.card h2{font:400 13px/1 "Exo 2",sans-serif;margin-bottom:12px}
.card p{font:400 7.4px/10.8px "Exo 2",sans-serif;text-align:left;color:var(--white)}
.card-why{left:58px;background:var(--gold)}.card-why h2{color:var(--navy)}
.card-how{left:259px;background:var(--navy)}.card-how h2{color:var(--gold);margin-top:6px}
.card-what{left:461px;background:var(--gold)}.card-what h2{color:var(--navy);margin-top:18px}

.coaches{left:0;top:553px;width:704px;height:262px;background:linear-gradient(180deg,var(--stadium-a),var(--stadium-b) 70%,#4e7a34)}
.section-title{left:0;width:704px;text-align:center;font:400 14px/1 "Exo 2",sans-serif}
.divider{left:260px;width:184px;height:12px}
.coach-panel{left:76px;top:80px;width:562px;height:112px;background:rgba(20,30,60,.35)}
.coach-photo{left:0;top:0;width:106px;height:110px;background:linear-gradient(135deg,#b8c0cc,#6c7584)}
.coach-bio{left:121px;top:2px;width:430px;font:400 7.4px/8.6px "Exo 2",sans-serif}
.coach-bio h3{font:500 8px/10px "Exo 2",sans-serif}
.coach-bio .by{color:var(--gold);font-size:8px;margin-bottom:6px}
.coach-bio p{margin-bottom:7px}
.slider-dots{top:244px;left:269px;width:166px;height:3px;display:flex;gap:5px}
.slider-dots span{flex:1;background:rgba(255,255,255,.35)}
.slider-dots span:first-child{background:var(--white)}

.members{left:0;top:815px;width:704px;height:205px;background:var(--light)}
.members-title{color:var(--navy);font-weight:500;top:21px;font-size:13px}
.members-title em{font-style:normal;color:var(--orange)}
.avatar-row{display:flex;gap:8px}
.avatar{width:40px;height:40px;border-radius:50%}
.row-one{left:62px;top:74px}.row-two{left:66px;top:135px}
.tone-a{background:linear-gradient(135deg,#d8c2a8,#7a5a44)}
.tone-b{background:linear-gradient(135deg,#9cc27a,#3f6a2a)}
.tone-c{background:linear-gradient(135deg,#e07070,#8c1f2a)}
.tone-d{background:linear-gradient(135deg,#8a8a7a,#3e3a30)}
.pager{left:334px;top:189px;width:27px;height:13px;background:#c8c8c8;border-radius:2px}

.newsletter{top:1020px;height:135px}
.newsletter-title{top:14px;font-size:13px;font-weight:500}
.email-field{left:106px;top:45px;width:387px;height:32px;border:1px solid rgba(255,255,255,.6);background:rgba(255,255,255,.12)}
.subscribe{left:493px;top:45px;width:100px;height:32px;background:var(--navy-deep);text-align:center;font:400 8px/32px "Exo 2",sans-serif}
.follow{left:288px;top:107px;font:500 6.5px/1 "Exo 2",sans-serif}
.social{left:323px;top:101px;width:90px;height:18px}

.site-footer{left:0;top:1155px;width:704px;height:45px;background:var(--footer)}
.footer-q{left:58px;top:8px;font:700 11px/1 "Carlito",sans-serif}
.footer-co{left:58px;top:28px;font:400 7px/10px "Exo 2",sans-serif;display:flex;align-items:center;gap:4px}
.footer-year{left:620px;top:18px;font:700 8px/1 "Exo 2",sans-serif}
</style>
</head>
<body>

<header class="site-header abs">
  <div class="brand brand-left abs">Junior Stride Athletics</div>
  <h1 class="tagline abs">Where Kids are Champions</h1>
  <div class="brand brand-right abs">Junior Stride Athletics</div>
</header>

<section class="hero abs" role="img" aria-label="Young children playing soccer on a training field">
  <h2 class="hero-title abs">Specialist sports coaching<br>for boys &amp; girls 5 to 16 years old</h2>
  <p class="hero-question abs">Is your child the next champion?<br><a href="#">Click here for details</a></p>
  <div class="trial-btn abs">TWO WEEK FREE TRIAL</div>
</section>

<section class="values grass-band abs" role="img" aria-label="Grass pitch background">
  <article class="card card-why abs">
    <h2>Why we do it</h2>
    <p>We are all about getting kids away from computer games and to start living life in a healthy and productive way. We aim to teach the kids how to play their chosen sport, have lots of FUN and help with their personal development for life's challenges. So whether you child wants to become a weekend warrior or just learn ...</p>
  </article>
  <article class="card card-how abs">
    <h2>How we do it</h2>
    <p>We start teaching boys &amp; girls from 5 years old basic skills of how to play their chosen sport. We introduce aspects of nutrition, fitness, physical preparation, injury prevention and other advanced concepts as your child progresses up until 16 years of age.</p>
  </article>
  <article class="card card-what abs">
    <h2>What we do</h2>
    <p>We hold weekly sessions for kids from 5 to 8, 9 to 12 and 12 to 16 years of age. We also have 3 day holiday programs and for those children that have talent and want to explore their chosen sport further we have elite squads.</p>
  </article>
</section>

<section class="coaches abs" role="img" aria-label="Stadium at dusk with a football on the turf">
  <h2 class="section-title abs" style="top:25px">Coaches – Australian Rules</h2>
  <svg class="divider abs" style="top:47px" viewBox="0 0 184 12"><line x1="0" y1="6" x2="184" y2="6" stroke="#c9d3e6" stroke-width=".8"/><circle cx="92" cy="6" r="5.5" fill="#6f86c4" stroke="#fff" stroke-width=".6"/></svg>
  <div class="coach-panel abs">
    <div class="coach-photo abs" role="img" aria-label="Coach standing in front of a sponsor wall"></div>
    <div class="coach-bio abs">
      <h3>About Daniel Ferris</h3>
      <div class="by">-Liam Corrick</div>
      <p>Daniel Ferris played over 200 games of football for Old Brackenfield, Elmsford &amp; Corrin Bay over his decade of playing the game. He is one who loves the game and wants to teach others how to play and have fun.</p>
      <p>In 2006 he reached out into coaching and over the past 10 years he has achieved arguably the best coaching record in local football including 4 senior premierships with Wattledown Wallabies, Ferndale and Kestrel Point. He has also coached junior teams and knows the difference between young kids playing the game for fun and professional weekend warriors.</p>
      <p>Let Daniel teach you child not just how to play Australian Rules football but also how to develop as a person into a more rounded and self confident person for the journey ahead of them.</p>
    </div>
  </div>
  <div class="slider-dots abs"><span></span><span></span><span></span></div>
</section>

<section class="members abs">
  <h2 class="section-title members-title abs"><em>Over 200 members and growing,</em>We love our team.</h2>
  <svg class="divider abs" style="top:40px" viewBox="0 0 184 12"><line x1="0" y1="6" x2="184" y2="6" stroke="#e2c46a" stroke-width=".8"/><circle cx="92" cy="6" r="5.5" fill="#3b5bb0" stroke="#fff" stroke-width=".6"/></svg>
  <div class="avatar-row row-one abs">
    <div class="avatar tone-a" role="img" aria-label="Member photo"></div><div class="avatar tone-b" role="img" aria-label="Member photo"></div><div class="avatar tone-c" role="img" aria-label="Member photo"></div><div class="avatar tone-d" role="img" aria-label="Member photo"></div><div class="avatar tone-b" role="img" aria-label="Member photo"></div><div class="avatar tone-a" role="img" aria-label="Member photo"></div><div class="avatar tone-c" role="img" aria-label="Member photo"></div><div class="avatar tone-a" role="img" aria-label="Member photo"></div><div class="avatar tone-d" role="img" aria-label="Member photo"></div><div class="avatar tone-a" role="img" aria-label="Member photo"></div><div class="avatar tone-b" role="img" aria-label="Member photo"></div><div class="avatar tone-a" role="img" aria-label="Member photo"></div>
  </div>
  <div class="avatar-row row-two abs">
    <div class="avatar tone-d" role="img" aria-label="Member photo"></div><div class="avatar tone-b" role="img" aria-label="Member photo"></div><div class="avatar tone-a" role="img" aria-label="Member photo"></div><div class="avatar tone-c" role="img" aria-label="Member photo"></div><div class="avatar tone-a" role="img" aria-label="Member photo"></div><div class="avatar tone-d" role="img" aria-label="Member photo"></div><div class="avatar tone-a" role="img" aria-label="Member photo"></div><div class="avatar tone-b" role="img" aria-label="Member photo"></div><div class="avatar tone-a" role="img" aria-label="Member photo"></div><div class="avatar tone-b" role="img" aria-label="Member photo"></div><div class="avatar tone-c" role="img" aria-label="Member photo"></div><div class="avatar tone-d" role="img" aria-label="Member photo"></div>
  </div>
  <svg class="pager abs" viewBox="0 0 27 13"><path d="M11 4 L8 6.5 L11 9 M16 4 L19 6.5 L16 9" fill="none" stroke="#fff" stroke-width="1"/></svg>
</section>

<section class="newsletter grass-band abs" role="img" aria-label="Grass pitch background">
  <h2 class="section-title newsletter-title abs">Sign up for our newsletter</h2>
  <div class="email-field abs"></div>
  <div class="subscribe abs">Subscribe</div>
  <span class="follow abs">Follow</span>
  <svg class="social abs" viewBox="0 0 90 18" aria-label="Social links">
    <circle cx="9" cy="9" r="8" fill="none" stroke="#fff" stroke-width="1"/>
    <circle cx="33" cy="9" r="8" fill="none" stroke="#fff" stroke-width="1"/>
    <circle cx="56" cy="9" r="8" fill="none" stroke="#fff" stroke-width="1"/>
    <circle cx="80" cy="9" r="8" fill="none" stroke="#fff" stroke-width="1"/>
  </svg>
</section>

<footer class="site-footer abs">
  <p class="footer-q abs">Have a question or comment</p>
  <p class="footer-co abs"><svg width="9" height="9" viewBox="0 0 9 9"><circle cx="4.5" cy="4.5" r="4" fill="none" stroke="#fff" stroke-width=".8"/><path d="M2.5 3.3h4v2.6h-4z M2.5 3.3 L4.5 4.8 L6.5 3.3" fill="none" stroke="#fff" stroke-width=".6"/></svg>Junior Stride Athletics Pty Ltd</p>
  <p class="footer-year abs">2016</p>
</footer>

</body>
</html>
```